Valdora Business Card Design - Professional Flexible and forward thinking. Clean and Easy to follow

Management Consulting Company. I focus on business development and concept and operational review. I need a progressive, simple and professional layout design for the business cards, letterhead and envelops
Professional Flexible and forward thinking. Clean and Easy to follow
Mature Business persons and professionals and Corporations

Target Market(s)

Mature Business persons and professionals and Corporations - Government org.

Industry/Entity Type

Consulting

Contact Information for Business Card

Requirements
Must have
• Marcus Valdora
• President
• Phone - 516.382.6047
• email - Mvaldora@valdorapartners.com
• Skype - Marc.valdora
• 7215 Pellham Avenue
• Suite A
• Cedarbrook, N.Y. 11742
• USA
Nice to have
• www.valdorapartners.com
Should not have
• N/A

```html
<!DOCTYPE html>
<html lang="en">
<head>
<meta charset="utf-8">
<title>Valdora Partners — Business Card</title>
<link rel="stylesheet" href="https://fonts.googleapis.com/css2?family=Cinzel:wght@400&family=Crimson+Text:wght@400;600&display=swap">
<style>
  :root {
    --page: #e9e6e1;
    --card-white: #ffffff;
    --gold: #f0b400;
    --gold-pale: #f5c94a;
    --gold-deep: #e08e00;
    --gold-light: #f6cd2a;
    --ink: #555555;
    --ink-soft: #7a7a7a;
  }
  * { margin: 0; padding: 0; box-sizing: border-box; }
  html, body { width: 1200px; height: 1024px; overflow: hidden; }
  body {
    background: var(--page);
    font-family: "Crimson Text", "Times New Roman", serif;
    position: relative;
  }
  .card {
    position: absolute;
    left: 232px;
    width: 736px;
    height: 420px;
    box-shadow: 0 6px 22px rgba(0,0,0,0.18);
    overflow: hidden;
  }
  /* Front */
  .card-front { top: 70px; background: var(--card-white); }
  .front-brand {
    position: absolute; left: 48px; top: 46px;
    display: flex; align-items: center; gap: 16px;
  }
  .brand-square { width: 46px; height: 46px; background: var(--gold); }
  .brand-name {
    font-family: "Cinzel", "Times New Roman", serif;
    font-size: 30px; color: var(--ink); letter-spacing: 0.5px;
  }
  .front-mark {
    position: absolute; right: 70px; top: 58px;
    width: 122px; height: 122px; background: var(--gold);
  }
  .person { position: absolute; left: 48px; top: 150px; }
  .person-name {
    font-family: "Cinzel", "Times New Roman", serif;
    font-size: 30px; color: var(--gold); letter-spacing: 0.5px;
  }
  .person-name .surname { color: var(--gold-pale); }
  .person-title {
    font-size: 14px; color: var(--ink-soft); letter-spacing: 1px;
    margin-top: 2px;
  }
  .person-rule {
    width: 255px; height: 1.5px; margin-top: 14px;
    background: linear-gradient(90deg, var(--gold), rgba(240,180,0,0.15));
  }
  .contacts { list-style: none; margin-top: 18px; }
  .contacts li {
    display: flex; align-items: center; gap: 12px;
    font-size: 19px; color: var(--ink); line-height: 30px;
  }
  .contacts svg { width: 16px; height: 16px; flex: none; }
  .address {
    position: absolute; right: 64px; top: 215px;
    font-size: 18px; line-height: 27px; color: var(--ink);
    font-style: normal;
  }

  /* Back */
  .card-back {
    top: 534px;
    background: radial-gradient(ellipse at 60% 35%, var(--gold-light), var(--gold) 45%, var(--gold-deep) 100%);
  }
  .back-brand {
    position: absolute; left: 56px; top: 78px;
    display: flex; align-items: center; gap: 24px;
  }
  .back-square { width: 92px; height: 92px; background: #ffffff; }
  .back-name {
    font-family: "Cinzel", "Times New Roman", serif;
    font-size: 44px; color: #ffffff; letter-spacing: 0.5px;
  }
  .back-web {
    position: absolute; left: 172px; top: 168px;
    font-size: 19px; color: #ffffff; letter-spacing: 0.5px;
  }
  .back-band {
    position: absolute; left: 0; right: 0; bottom: 0; height: 108px;
    background: #ffffff;
    padding: 12px 0;
  }
  .back-band-pattern {
    width: 100%; height: 100%;
    background: linear-gradient(180deg, #5a5a5a, #8a8a8a);
  }
</style>
</head>
<body>
  <section class="card card-front" aria-label="Business card front">
    <div class="front-brand">
      <span class="brand-square"></span>
      <span class="brand-name">VALDORA PARTNERS</span>
    </div>
    <div class="front-mark"></div>

    <div class="person">
      <div class="person-name">MARCUS <span class="surname">VALDORA</span></div>
      <div class="person-title">PRESIDENT</div>
      <div class="person-rule"></div>
      <ul class="contacts">
        <li>
          <svg viewBox="0 0 16 16" aria-hidden="true"><rect width="16" height="16" rx="3" fill="#f0b400"/><path d="M5 3.5c.6 0 1.4 1.8 1.4 2.3 0 .6-.9.8-.9 1.3.3 1.2 1.3 2.2 2.5 2.6.5 0 .7-.9 1.3-.9.5 0 2.2.8 2.2 1.4 0 .9-1 1.8-2 1.8C6.2 12 4 9.8 3.9 6.5c0-1 .3-3 1.1-3z" fill="#fff"/></svg>
          516.382.6047
        </li>
        <li>
          <svg viewBox="0 0 16 16" aria-hidden="true"><rect width="16" height="16" rx="3" fill="#f0b400"/><rect x="3.5" y="5" width="9" height="6.5" fill="none" stroke="#fff" stroke-width="1.2"/><path d="M3.5 5l4.5 3.6L12.5 5" fill="none" stroke="#fff" stroke-width="1.2"/></svg>
          Mvaldora@valdorapartners.com
        </li>
        <li>
          <svg viewBox="0 0 16 16" aria-hidden="true"><circle cx="8" cy="8" r="8" fill="#f0b400"/></svg>
          Marc.valdora
        </li>
      </ul>
    </div>

    <address class="address">
      7215 Pellham Avenue, Suite A<br>
      Cedarbrook, N.Y. 11742<br>
      USA
    </address>
  </section>

  <section class="card card-back" aria-label="Business card back">
    <div class="back-brand">
      <span class="back-square"></span>
      <span class="back-name">VALDORA PARTNERS</span>
    </div>
    <div class="back-web">www.valdorapartners.com</div>
    <div class="back-band">
      <div class="back-band-pattern" role="img" aria-label="Grey diagonal stripe pattern band"></div>
    </div>
  </section>
</body>
</html>
```